Business Card Design for an international medical business

We need a professional and elegant business card design with fashionable graphic element. Our company is located in Hong Kong with three worldwide production lines for medical equipment(surgical face masks, N95, face shields and so on). Our factories all contain medical standard ISOs and all product fulfill Garrow lab and KTR testing standards.

We would like to see designs that show the impression of our professional expertise, formal corporate image with creative thinking work style and inspiring global concept. We want the content in both English and Japanese on the same card. We also want to print our the patent trade mark and company logo on the card.

Target Market(s)

Southeast Asia, US, EU

Industry/Entity Type

Medical Equipment

Contact Information for Business Card

Below are the content we want to be shown on the business card(please help us to simplified them to be more presentable and readable):

Company name: Brightmoor (Hong Kong) 5K Medical Technology Company Limited
Address: Unit 2204, 22/F, Pine Court, No.8 Ferndale Road, Kwun Lam, Hong Kong.
Band Name: B5K
Homepage: www.brightmoor5kq.com
Name: Lok Wing Fei
Title: Manager
Tel: +852-xxxx-xxxx
Mobile: +852-xxxx-xxxx
Email: xx@brightmoor5kq.com

Production Lines:
China: Ping Shan Kai Lok Medical Technology Company Limited
Mo Tan City Ren Bo Textile Machinery Company Limited
Bangladesh: B5K Medical Technology Company Limited

Qualifications:
ISO 13485:2016
ISO 14644-1:2015
ISO Class 8 Cleanroom
ASTM F2100 Level 2
EN14683 Type IIR
EN149 FFP2
CE Certified
FDA Registration number: XXX

Requirements
Must have
• use pantone color for the design
and provide the pantone number for printing purpose
Should not have
• Background color should not be black.

```html
<!DOCTYPE html>
<html lang="en">
<head>
<meta charset="utf-8">
<title>B5K Business Card</title>
<link href="https://fonts.googleapis.com/css2?family=Montserrat:wght@700;800&family=Arimo:wght@400;700&display=swap" rel="stylesheet">
<style>
  :root{
    --teal:#1bbcc0;
    --mauve:#7c6f99;
    --pink:#f2005a;
    --ink:#1c1c1c;
    --rule:#c9c9c9;
    --paper:#ffffff;
    --stage:#e4e5e8;
  }
  *{box-sizing:border-box;margin:0;padding:0}
  html,body{width:1200px;height:1015px;overflow:hidden}
  body{background:var(--stage);font-family:"Arimo",Arial,sans-serif;position:relative}
  .card{position:absolute;left:250px;width:700px;height:400px;box-shadow:0 10px 30px rgba(0,0,0,.18);overflow:hidden}
  .card--front{top:60px;color:#fff;
    background:linear-gradient(200deg,var(--teal) 0%,#3aa8b8 22%,var(--mauve) 48%,#c23c78 72%,var(--pink) 100%)}
  .card--back{top:555px;background:var(--paper);color:var(--ink)}

  .deco-circle{position:absolute;right:150px;top:40px;width:230px;height:230px;border-radius:50%;
    background:rgba(70,120,160,.25)}

  .brand{position:absolute;left:42px;top:40px;display:flex;align-items:center;gap:14px}
  .brand__dot{width:22px;height:22px;border-radius:50%;background:#fff}
  .brand__name{font-family:"Montserrat",sans-serif;font-weight:800;font-size:56px;letter-spacing:3px;color:#fff;line-height:1}

  .lines{position:absolute;left:42px;top:150px;font-size:17px;line-height:1.3}
  .heading{font-family:"Montserrat",sans-serif;font-weight:800;font-size:17px;letter-spacing:.5px;margin-bottom:4px}
  .country{font-family:"Montserrat",sans-serif;font-weight:800;font-size:19px}

  .quals{position:absolute;right:40px;top:80px;text-align:right;font-size:17px;line-height:1.28}
  .fda{position:absolute;right:40px;bottom:38px;font-size:17px}

  .logo{position:absolute;left:40px;top:160px;display:flex;align-items:center;gap:12px}
  .logo__dot{width:18px;height:18px;border-radius:50%;background:var(--pink);flex:none}
  .logo__text{border-left:1px solid var(--teal);padding-left:10px}
  .logo__name{font-family:"Montserrat",sans-serif;font-weight:800;font-size:31px;color:var(--pink);line-height:1}
  .logo__sub{font-family:"Montserrat",sans-serif;font-weight:700;font-size:9.5px;color:var(--teal);margin-top:5px}

  .divider{position:absolute;left:380px;top:60px;width:1px;height:280px;background:var(--rule)}

  .contact{position:absolute;left:405px;top:70px}
  .contact__name{font-family:"Montserrat",sans-serif;font-weight:800;font-size:24px;color:var(--pink);text-transform:uppercase;line-height:1}
  .contact__title{font-size:16px;margin:3px 0 12px}
  .contact__list{list-style:none;font-size:15px;line-height:1.55}
  .contact__list li{display:flex;align-items:center;gap:10px}
  .contact__list svg{width:15px;height:15px;flex:none}
  .web{color:var(--pink)}
  .address{font-size:15.5px;line-height:1.35;margin-top:16px}
</style>
</head>
<body>
  <section class="card card--front">
    <div class="deco-circle" role="img" aria-label="Large faint brand symbol decoration"></div>
    <div class="brand"><span class="brand__dot"></span><span class="brand__name">B5K</span></div>
    <div class="lines">
      <p class="heading">PRODUCTION LINES</p>
      <p class="country">China</p>
      <p>Ping Shan Kai Lok Medical<br>Technology Company Limited</p>
      <p>Mo Tan City Ren Bo Textile<br>Machinery Company Limited</p>
      <p class="country">Bangladesh</p>
      <p>B5K Medical Technology<br>Company Limited</p>
    </div>
    <div class="quals">
      <p class="heading">QUALIFICATIONS</p>
      <p>ISO 13485:2016</p>
      <p>ISO 14644-1:2015</p>
      <p>ISO Class 8 Cleanroom</p>
      <p>ASTM F2100 Level 2</p>
      <p>EN14683 Type IIR</p>
      <p>EN149 FFP2</p>
      <p>CE Certified</p>
    </div>
    <p class="fda">FDA Registration number: XXX</p>
  </section>

  <section class="card card--back">
    <div class="logo">
      <span class="logo__dot"></span>
      <div class="logo__text">
        <p class="logo__name">BRIGHTMOOR</p>
        <p class="logo__sub">5K Medical Technology Company Limited</p>
      </div>
    </div>
    <div class="divider"></div>
    <div class="contact">
      <p class="contact__name">Lok Wing Fei</p>
      <p class="contact__title">Manager</p>
      <ul class="contact__list">
        <li><svg viewBox="0 0 16 16"><path d="M3 1l3 3-2 2c1 2 3 4 5 5l2-2 3 3-2 3C7 15 1 9 1 3z" fill="var(--pink)"/></svg>+852-xxxx-xxxx</li>
        <li><svg viewBox="0 0 16 16"><rect x="4" y="1" width="8" height="14" rx="1.5" fill="none" stroke="var(--pink)" stroke-width="1.6"/><circle cx="8" cy="12.5" r="1" fill="var(--pink)"/></svg>+852-xxxx-xxxx</li>
        <li><svg viewBox="0 0 16 16"><rect x="1" y="3" width="14" height="10" fill="var(--pink)"/><path d="M1 3l7 6 7-6" fill="none" stroke="#fff" stroke-width="1.2"/></svg>xx@brightmoor5kq.com</li>
        <li><svg viewBox="0 0 16 16"><circle cx="8" cy="8" r="6.5" fill="none" stroke="var(--pink)" stroke-width="1.4"/><ellipse cx="8" cy="8" rx="3" ry="6.5" fill="none" stroke="var(--pink)" stroke-width="1.2"/><path d="M1.5 8h13M2.5 5h11M2.5 11h11" stroke="var(--pink)" stroke-width="1"/></svg><span class="web">www.brightmoor5kq.com</span></li>
      </ul>
      <p class="address">Unit 2204, 22/F, Pine Court<br>No.8 Ferndale Road<br>Kwun Lam, Hong Kong.</p>
    </div>
  </section>
</body>
</html>
```